Retail Jewelry Business Card Design Project

We are in need of a new business card design for a retail jewelry store. This store is in the business of fine jewelry including but not specific to bridal jewelry, diamonds, designer jewelry and watches.

This store has been in business for 20 years but continues to strive for a modern professional appeal. The main colors use for this business are a royal blue, white and silver.

Target Market(s)

Target market is ages 18-50

Industry/Entity Type

Jewelry

Requirements
Must have
• Sales Person Name
Sales Person Email Address

Store Address
Store Phone
Website

Standard business card size. No odd shapes or sizes.
Nice to have
• Overall modern feel for card.

We have thought that a design with a nice feature of the logo on the back of the card would be nice but open to ideas.
Should not have
• No specific images of jewelry should be used.

```html
<!DOCTYPE html>
<html lang="en">
<head>
<meta charset="utf-8">
<title>Marlowe Reed Fine Jewelry – Business Cards</title>
<link href="https://fonts.googleapis.com/css2?family=Jost:wght@400&display=swap" rel="stylesheet">
<style>
  :root {
    --page: #e4e5e7;
    --royal: #1f45a8;
    --royal-bright: #0b5bc0;
    --royal-deep: #1d3f9e;
    --band: #1c1b1d;
    --silver: #c9d3e6;
    --white: #ffffff;
  }
  * { box-sizing: border-box; margin: 0; padding: 0; }
  html, body {
    width: 1200px; height: 1200px; overflow: hidden;
    background: var(--page);
    font-family: "Jost", "Futura", sans-serif;
    font-weight: 400;
    color: var(--white);
  }
  .sheet {
    position: relative; width: 1200px; height: 1200px;
    display: flex; flex-direction: column; align-items: center; justify-content: center;
    gap: 60px;
  }
  .card {
    position: relative; width: 820px; height: 469px; overflow: hidden;
    box-shadow: 0 6px 18px rgba(0,0,0,0.18);
  }
  /* Front */
  .card--front {
    background: linear-gradient(135deg, var(--royal-bright) 0%, var(--royal) 70%, var(--royal-deep) 100%);
  }
  .jewel-visual {
    position: absolute; left: 0; top: 0; width: 330px; height: 300px;
    background:
      radial-gradient(circle at 52% 58%, rgba(235,240,250,0.85) 0 14%, rgba(190,205,230,0.35) 22%, transparent 40%),
      radial-gradient(circle at 70% 22%, rgba(230,236,248,0.7) 0 9%, transparent 22%),
      radial-gradient(ellipse at 30% 70%, rgba(160,195,255,0.35), transparent 60%);
  }
  .brand {
    position: absolute; text-align: center; line-height: 1;
    color: var(--white);
  }
  .brand__name { display: block; }
  .brand__tag { display: block; letter-spacing: 0.22em; }
  .card--front .brand { right: 70px; top: 150px; width: 330px; }
  .card--front .brand__name { font-size: 50px; }
  .card--front .brand__tag { font-size: 19px; margin-top: 12px; }

  .info-band {
    position: absolute; left: 0; top: 300px; width: 100%; height: 128px;
    background: var(--band);
    border-top: 3px solid var(--silver);
    display: flex; align-items: center;
  }
  .contact-person {
    width: 400px; padding-right: 22px; text-align: right;
  }
  .contact-person__name { font-size: 23px; letter-spacing: 0.01em; }
  .contact-person__email { font-size: 18px; margin-top: 4px; }
  .divider {
    width: 2px; height: 70px;
    background: linear-gradient(to bottom, transparent, var(--silver), transparent);
  }
  .store-details {
    padding-left: 22px; font-size: 19px; line-height: 1.3;
  }
  .store-details p { margin: 0; }

  /* Back */
  .card--back {
    background: radial-gradient(ellipse at 55% 45%, var(--royal-bright) 0%, var(--royal) 55%, var(--royal-deep) 100%);
    display: flex; align-items: center; justify-content: center;
  }
  .card--back .brand { position: static; }
  .card--back .brand__name { font-size: 66px; }
  .card--back .brand__tag { font-size: 24px; margin-top: 16px; }
</style>
</head>
<body>
<main class="sheet">
  <section class="card card--front" aria-label="Business card front">
    <div class="jewel-visual" role="img" aria-label="Photograph of a sparkling diamond pendant with starry glints"></div>
    <div class="brand">
      <span class="brand__name">Marlowe Reed</span>
      <span class="brand__tag">FINE JEWELRY</span>
    </div>
    <div class="info-band">
      <div class="contact-person">
        <p class="contact-person__name">MARLOWE REED HALVORSEN</p>
        <p class="contact-person__email">marlowe@marlowereedjewelry.com</p>
      </div>
      <div class="divider"></div>
      <address class="store-details" style="font-style:normal">
        <p>2290 Linden Avenue</p>
        <p>Bayport, FL 32555</p>
        <p>www.marlowereedjewelry.com</p>
      </address>
    </div>
  </section>

  <section class="card card--back" aria-label="Business card back">
    <div class="brand">
      <span class="brand__name">Marlowe Reed</span>
      <span class="brand__tag">FINE JEWELRY</span>
    </div>
  </section>
</main>
</body>
</html>
```